Design 5 colour schemes for one web page

We are looking for 5 different colour schemes for our product template to create different kinds of colour tone for our web page, it doesn't need to be restructure the layout, just need to provide different color solution.

Please refer to the attached images and take note of the following when you’re working on the design:
(1) Please precisely reproduce the layout. Cannot remove or delete any wordings, components or column shown in the images.
(2) Okay to revise icons, background color or text style as you prefer. But cannot move/delete them.
(3) Provide PSD source files with good layer management. HTML/CSS are not required.
(4) Make reasonable and professional design.

After completion, please send back:
(1) 5 images with 5 different colour schemes.
(2) Related PSD files.

Industry/Entity Type

Management

Number of Pages Required

1 page

Font styles to use
Serif
Sans Serif

Requirements
Must have
• (1) 5 images for the colour schemes.
• (2) 5 PSD source files with good layer management.
Nice to have
• (1) Explanation about your design of the colour schemes.
Should not have
• (1) HTML/CSS code are not required.

```html
<!DOCTYPE html>
<html lang="en">
<head>
<meta charset="utf-8">
<title>Sportsbook – Sports</title>
<link rel="stylesheet" href="https://fonts.googleapis.com/css2?family=Source+Sans+3:wght@400;600;700&display=swap">
<style>
:root{
  --accent:#e8771e;
  --accent-dark:#c9620f;
  --accent-soft:#f1a25f;
  --navy:#1f2a44;
  --navy-deep:#172036;
  --navy-line:#141b2e;
  --top:#18213a;
  --bg:#dfe3ea;
  --header:#f1f3f7;
  --subbar:#e2e6ed;
  --panel:#ffffff;
  --line:#d3d8e1;
  --text:#1c2336;
  --muted:#4d566b;
  --subtle:#aab3c5;
}
*{box-sizing:border-box;margin:0;padding:0}
html,body{width:756px;height:1200px;overflow:hidden}
body{font-family:"Source Sans 3",Arial,sans-serif;color:var(--text);background:var(--bg);position:relative}
.abs{position:absolute}
.acc{fill:var(--accent)}
.wht{fill:#fff}
.ink{fill:var(--text)}

/* top strip */
.topbar{left:0;top:0;width:756px;height:30px;background:var(--top);color:#fff}
.topbar .links{position:absolute;left:18px;top:9px;font-size:8.5px;line-height:10px;display:flex;gap:7px}
.topbar .links .sep{color:var(--subtle)}
.balance{position:absolute;left:606px;top:4px}
.balance small{display:block;font-size:6.5px;line-height:8px;color:var(--subtle);letter-spacing:.2px}
.balance b{display:block;font-size:12.5px;line-height:15px;font-weight:700}
.bars{position:absolute;left:678px;top:5px}

/* header */
.header{left:0;top:30px;width:756px;height:46px;background:var(--header)}
.brand{position:absolute;left:0;top:0;width:122px;height:46px;background:var(--accent);color:#fff;font-size:29px;font-weight:400;display:flex;align-items:center;justify-content:center}
.nav{position:absolute;left:287px;top:0;height:46px;display:flex;font-size:12px;font-weight:400}
.nav a{display:flex;align-items:center;padding:0 12px;color:var(--text);text-decoration:none;height:46px}
.nav a.active{background:var(--navy);color:#fff;padding:0 12px}
.avatar{position:absolute;left:625px;top:7px;width:31px;height:31px;border-radius:50%;background:linear-gradient(#b9a58f,#6f5c4a);border:2px solid #fff;box-shadow:0 0 0 1px #8a93a6}
.user{position:absolute;left:662px;top:13px;font-size:15px;line-height:18px;color:var(--text)}

/* sub bar */
.subbar{left:0;top:76px;width:756px;height:26px;background:var(--subbar);font-size:9.5px}
.subbar .item{position:absolute;top:0;height:26px;display:flex;align-items:center;gap:5px}
.favbtn{position:absolute;left:499px;top:1px;width:32px;height:24px;background:var(--accent);display:flex;align-items:center;justify-content:center;gap:3px}
.vsep{position:absolute;top:5px;width:1px;height:16px;background:#a3abbb}

/* sidebar */
.side{left:0;top:114px;width:122px}
.side-head{height:43px;background:var(--navy);color:var(--accent);text-align:center;font-size:10px;padding-top:7px;position:relative}
.side-head .caret{position:absolute;right:14px;top:18px}
.sport{height:42.95px;display:flex;border-bottom:1px solid var(--navy-line);font-size:9px;color:#fff}
.sport .ic{width:26px;background:var(--accent);display:flex;align-items:center;justify-content:center;border-bottom:1px solid var(--accent-dark)}
.sport .name{flex:1;background:var(--navy);display:flex;align-items:center;justify-content:space-between;padding:0 7px 0 8px}
.ticket{height:42px;background:var(--navy);color:var(--accent);text-align:center;font-size:10px;padding-top:6px;position:relative}
.mybets{height:55px;background:#d2d8e2;text-align:center;padding-top:14px}
.mybets h4{font-size:10px;font-weight:400;color:var(--muted)}
.mybets p{font-size:7.5px;color:var(--muted);margin-top:4px}
.btns{display:flex;height:22px;font-size:7.5px;font-weight:600;color:#fff}
.btns div{flex:1;display:flex;align-items:center;justify-content:center}
.btns .refresh{background:var(--accent)}
.btns .all{background:var(--navy-deep)}
.copy{left:0;top:1159px;width:130px;text-align:center;font-size:7.5px;color:var(--muted);line-height:15px}
.footlinks{left:240px;top:1173px;font-size:7.5px;color:var(--muted);display:flex;gap:7px}

/* panels */
.panel-head{position:absolute;left:137px;width:619px;height:23px;background:var(--accent);color:#fff;font-size:9.5px}
.panel-head .title{position:absolute;left:12px;top:0;height:23px;display:flex;align-items:center;gap:6px}
.panel-head .count{position:absolute;left:228px;top:0;height:23px;display:flex;align-items:center;gap:5px}
.panel-head .league{position:absolute;left:524px;top:0;height:23px;display:flex;align-items:center;gap:6px}

.colhead{position:absolute;left:137px;width:619px;height:48px;background:var(--panel);display:grid;
  grid-template-columns:58px 99px 44px 41px 41px 44px 50px 72px 47px 83px 40px;
  grid-template-rows:22px 26px;font-size:9.5px;border-bottom:1px solid var(--line)}
.colhead div{display:flex;align-items:center;justify-content:center;border-left:1px solid var(--line);border-top:1px solid var(--line)}
.colhead .time{grid-row:1/3;grid-column:1;border-left:none}
.colhead .events{grid-row:1/3;grid-column:2}
.colhead .ft{grid-column:3/7;grid-row:1;border-top:none}
.colhead .fh{grid-column:7/11;grid-row:1;border-top:none}
.colhead .more{grid-row:1/3;grid-column:11}
.colhead .r2{grid-row:2}
.colhead .blank{grid-column:10;grid-row:2}

.league-bar{position:absolute;left:137px;width:619px;height:22px;background:var(--navy);color:#fff;font-size:9px;display:flex;align-items:center;gap:6px;padding-left:10px}

.matches{position:absolute;left:137px;width:619px;background:var(--panel)}
.match{display:grid;grid-template-columns:25px 33px 99px 44px 41px 41px 44px 252px 40px;border-bottom:1px solid var(--line);font-size:8.5px;line-height:11px;height:52.3px}
.match>div{display:flex;align-items:center;justify-content:center}
.match .stat{border-right:1px solid var(--line)}
.match .tm{flex-direction:column;border-right:1px solid var(--line)}
.match .ev{flex-direction:column;align-items:flex-start;justify-content:center;padding-left:4px;border-right:1px solid var(--line);font-size:8px}
.match .od{flex-direction:column}
.match .ou{align-items:flex-start;padding-top:13px}
.match .x12{flex-direction:column;border-right:1px solid var(--line)}
.match .mr{gap:2px;font-size:9px}
.match:last-child{border-bottom:none}

/* user menu */
.menu{left:611px;top:70px;width:126px;height:99px;background:var(--navy);color:#fff;font-size:9.5px}
.menu .mi{height:25px;display:flex;align-items:center;gap:9px;padding-left:8px}
.menu .mi.logout{background:var(--accent);height:24px}
</style>
</head>
<body>

<div class="abs topbar">
  <div class="links"><span>My Bets</span><span class="sep">|</span><span>Statement</span><span class="sep">|</span><span>Preferences</span><span class="sep">|</span><span>Announcments</span></div>
  <div class="balance"><small>MY BALANCE</small><b>$21,561.01</b></div>
  <svg class="bars" width="60" height="22" viewBox="0 0 60 22" aria-hidden="true">
    <g class="acc"><rect x="0" y="11" width="3" height="11"/><rect x="5" y="6" width="3" height="16"/><rect x="10" y="2" width="3" height="20"/><rect x="15" y="0" width="3" height="22"/><rect x="20" y="5" width="3" height="17"/><rect x="25" y="9" width="3" height="13"/><rect x="30" y="13" width="3" height="9"/><rect x="35" y="16" width="3" height="6"/><rect x="40" y="19" width="3" height="3"/><rect x="45" y="17" width="3" height="5"/><rect x="50" y="19" width="3" height="3"/><rect x="55" y="13" width="3" height="9"/></g>
  </svg>
</div>

<div class="abs header">
  <div class="brand">Logo</div>
  <nav class="nav"><a>Home</a><a class="active">Sports</a><a>Live Sports</a><a>Live Casino</a></nav>
  <div class="avatar" role="img" aria-label="User profile photo"></div>
  <div class="user">Jhon Doe <svg width="8" height="6" viewBox="0 0 8 6"><path class="ink" d="M0 0h8L4 5z"/></svg></div>
</div>

<div class="abs subbar">
  <div class="item" style="left:17px">
    <svg width="15" height="15" viewBox="0 0 16 16" aria-hidden="true"><circle cx="8" cy="8" r="7" fill="none" stroke="#1c2336" stroke-width="1.3"/><path d="M1 8h14M8 1c-3 4-3 10 0 14M8 1c3 4 3 10 0 14" fill="none" stroke="#1c2336" stroke-width="1.1"/></svg>
    <span>English (Asia)</span>
    <svg width="8" height="5" viewBox="0 0 8 5"><path class="ink" d="M0 0h8L4 5z"/></svg>
  </div>
  <div class="vsep" style="left:122px"></div>
  <div class="item" style="left:136px">
    <svg width="16" height="15" viewBox="0 0 16 15" aria-hidden="true"><rect x="1" y="2" width="14" height="12" fill="none" stroke="#1c2336" stroke-width="1.3"/><path d="M1 5h14M4 0v3M12 0v3M4 8h2M8 8h2M12 8h1M4 11h2M8 11h2" stroke="#1c2336" stroke-width="1.3"/></svg>
    <span>Nob, 19, 2014 11 : 40 AM</span>
  </div>
  <div class="favbtn">
    <svg width="11" height="11" viewBox="0 0 12 12"><path class="wht" d="M6 0l1.8 3.9 4.2.4-3.2 2.8 1 4.1L6 9 2.2 11.2l1-4.1L0 4.3l4.2-.4z"/></svg>
    <svg width="6" height="4" viewBox="0 0 6 4"><path class="wht" d="M0 0h6L3 4z"/></svg>
  </div>
  <svg class="abs" style="left:542px;top:6px" width="16" height="15" viewBox="0 0 16 15" aria-hidden="true"><rect x="1" y="1" width="11" height="12" fill="none" stroke="#1c2336" stroke-width="1.2"/><path d="M3 4h7M3 7h5M3 10h4" stroke="#1c2336"/><circle cx="12" cy="11" r="3.5" fill="#e2e6ed" stroke="#1c2336"/><path d="M12 9v4M10 11h4" stroke="#1c2336"/></svg>
  <div class="vsep" style="left:576px"></div>
  <svg class="abs" style="left:591px;top:7px" width="15" height="13" viewBox="0 0 15 13" aria-hidden="true"><path class="ink" d="M0 4h3l4-4v13L3 9H0z"/><path d="M9 4c1 1 1 4 0 5M11 2c2 2 2 7 0 9" stroke="#1c2336" fill="none"/></svg>
</div>

<aside class="abs side">
  <div class="side-head">
    <svg width="8" height="10" viewBox="0 0 8 10"><path class="acc" d="M0 0h8v2c0 2-2 3-3 3v3h2v2H1V8h2V5C2 5 0 4 0 2z"/></svg>
    <div>SPORTS</div>
    <svg class="caret" width="8" height="5" viewBox="0 0 8 5"><path class="acc" d="M0 0h8L4 5z"/></svg>
  </div>
  <div class="sport"><div class="ic"><svg width="12" height="12"><circle cx="6" cy="6" r="4" fill="none" stroke="#fff" stroke-width="1.4"/></svg></div><div class="name"><span>Football</span><span>600</span></div></div>
  <div class="sport"><div class="ic"><svg width="12" height="12"><circle cx="6" cy="6" r="4" fill="none" stroke="#fff" stroke-width="1.4"/></svg></div><div class="name"><span>Basketball</span><span>600</span></div></div>
  <div class="sport"><div class="ic"><svg width="12" height="12"><circle cx="6" cy="6" r="4" fill="none" stroke="#fff" stroke-width="1.4"/></svg></div><div class="name"><span>Baseball</span><span>600</span></div></div>
  <div class="sport"><div class="ic"><svg width="12" height="12"><circle cx="6" cy="6" r="4" fill="none" stroke="#fff" stroke-width="1.4"/></svg></div><div class="name"><span>Tennis</span><span>600</span></div></div>
  <div class="sport"><div class="ic"><svg width="12" height="12"><circle cx="6" cy="6" r="4" fill="none" stroke="#fff" stroke-width="1.4"/></svg></div><div class="name"><span>US Football</span><span>600</span></div></div>
  <div class="sport"><div class="ic"><svg width="12" height="12"><circle cx="6" cy="6" r="4" fill="none" stroke="#fff" stroke-width="1.4"/></svg></div><div class="name"><span>Badminton</span><span>600</span></div></div>
  <div class="sport"><div class="ic"><svg width="12" height="12"><circle cx="6" cy="6" r="4" fill="none" stroke="#fff" stroke-width="1.4"/></svg></div><div class="name"><span>Boxing</span><span>600</span></div></div>
  <div class="sport"><div class="ic"><svg width="12" height="12"><circle cx="6" cy="6" r="4" fill="none" stroke="#fff" stroke-width="1.4"/></svg></div><div class="name"><span>Cricket</span><span>600</span></div></div>
  <div class="sport"><div class="ic"><svg width="12" height="12"><circle cx="6" cy="6" r="4" fill="none" stroke="#fff" stroke-width="1.4"/></svg></div><div class="name"><span>Cycling</span><span>600</span></div></div>
  <div class="sport"><div class="ic"><svg width="12" height="12"><circle cx="6" cy="6" r="4" fill="none" stroke="#fff" stroke-width="1.4"/></svg></div><div class="name"><span>Darts</span><span>600</span></div></div>
  <div class="sport"><div class="ic"><svg width="12" height="12"><circle cx="6" cy="6" r="4" fill="none" stroke="#fff" stroke-width="1.4"/></svg></div><div class="name"><span>Entertainment</span><span>600</span></div></div>
  <div class="sport"><div class="ic"><svg width="12" height="12"><circle cx="6" cy="6" r="4" fill="none" stroke="#fff" stroke-width="1.4"/></svg></div><div class="name"><span>Golf</span><span>600</span></div></div>
  <div class="sport"><div class="ic"><svg width="12" height="12"><circle cx="6" cy="6" r="4" fill="none" stroke="#fff" stroke-width="1.4"/></svg></div><div class="name"><span>Handball</span><span>600</span></div></div>
  <div class="sport"><div class="ic"><svg width="12" height="12"><circle cx="6" cy="6" r="4" fill="none" stroke="#fff" stroke-width="1.4"/></svg></div><div class="name"><span>Ice Hockey</span><span>600</span></div></div>
  <div class="sport"><div class="ic"><svg width="12" height="12"><circle cx="6" cy="6" r="4" fill="none" stroke="#fff" stroke-width="1.4"/></svg></div><div class="name"><span>Martial Arts</span><span>600</span></div></div>
  <div class="sport"><div class="ic"><svg width="12" height="12"><circle cx="6" cy="6" r="4" fill="none" stroke="#fff" stroke-width="1.4"/></svg></div><div class="name"><span>Motor Sports</span><span>600</span></div></div>
  <div class="sport"><div class="ic"><svg width="12" height="12"><circle cx="6" cy="6" r="4" fill="none" stroke="#fff" stroke-width="1.4"/></svg></div><div class="name"><span>Snooker</span><span>600</span></div></div>
  <div class="sport"><div class="ic"><svg width="12" height="12"><circle cx="6" cy="6" r="4" fill="none" stroke="#fff" stroke-width="1.4"/></svg></div><div class="name"><span>Rugby</span><span>600</span></div></div>
  <div class="sport"><div class="ic"><svg width="12" height="12"><circle cx="6" cy="6" r="4" fill="none" stroke="#fff" stroke-width="1.4"/></svg></div><div class="name"><span>Voleyball</span><span>600</span></div></div>
  <div class="sport"><div class="ic"><svg width="12" height="12"><circle cx="6" cy="6" r="4" fill="none" stroke="#fff" stroke-width="1.4"/></svg></div><div class="name"><span>Winter Sports</span><span>600</span></div></div>
  <div class="ticket">
    <svg width="14" height="12" viewBox="0 0 14 12"><path d="M7 0l7 6-7 6-7-6z" fill="none" stroke="#e8771e" stroke-width="1.3"/></svg>
    <div>TICKET</div>
    <svg class="abs" style="right:14px;top:19px" width="8" height="5" viewBox="0 0 8 5"><path class="acc" d="M0 0h8L4 5z"/></svg>
  </div>
  <div class="mybets"><h4>MY BETS</h4><p>No Pending Bets</p></div>
  <div class="btns"><div class="refresh">REFRESH</div><div class="all">VIEW ALL</div></div>
</aside>

<div class="abs copy">© 2014 - Betting<br>All Rights Reserved.</div>
<div class="abs footlinks"><span>Betting Rules</span><span>|</span><span>Contact Us</span><span>|</span><span>Privacy Policy</span><span>|</span><span>Responsible Gambling</span><span>|</span><span>Terms &amp; Conditions</span><span>|</span><span>Tutorials</span></div>

<!-- today live -->
<div class="panel-head" style="top:116px">
  <div class="title"><svg width="9" height="12" viewBox="0 0 9 12"><circle class="wht" cx="5" cy="1.6" r="1.6"/><path d="M4 4l-3 3M4 4v4l-2 4M4 8l3 4M4 5l3 1" stroke="#fff" stroke-width="1.3" fill="none"/></svg>TODAY LIVE</div>
  <div class="count"><svg width="12" height="12" viewBox="0 0 12 12"><circle cx="6" cy="6" r="4.5" fill="none" stroke="#fff" stroke-width="2" stroke-dasharray="5 2"/></svg>38 New Events</div>
  <div class="league"><svg width="8" height="10" viewBox="0 0 8 10"><path class="wht" d="M0 0h8v2c0 2-2 3-3 3v3h2v2H1V8h2V5C2 5 0 4 0 2z"/></svg>Select League</div>
</div>
<div class="colhead" style="top:139px">
  <div class="time">Time</div><div class="events">Events</div>
  <div class="ft">Full Time</div><div class="fh">First Half</div><div class="more">More</div>
  <div class="r2" style="grid-column:3">A 1×2</div><div class="r2" style="grid-column:4">HDP</div><div class="r2" style="grid-column:5">OU</div><div class="r2" style="grid-column:6">1×2</div>
  <div class="r2" style="grid-column:7">HDP</div><div class="r2" style="grid-column:8">OU</div><div class="r2" style="grid-column:9">1×2</div><div class="blank"></div>
</div>
<div class="league-bar" style="top:186px">★ <span>Coastal Premier League</span></div>
<div class="matches" style="top:208px">
  <div class="match" style="height:54px"><div class="stat"><svg width="11" height="9" viewBox="0 0 11 9"><path class="acc" d="M0 9V5h2v4zM3 9V3h2v6zM6 9V1h2v8zM9 9V4h2v5z"/></svg></div><div class="tm"><span>16 : 30</span><span>Live</span></div><div class="ev"><span>Harbour Coast Rovers</span><span>Southbank Victors</span></div><div>0-0.5</div><div class="od"><span>0.77</span><span>-0.95</span></div><div class="ou">6-6.5</div><div class="x12"><span>O -0.85</span><span>U -0.65</span></div><div></div><div class="mr"><svg width="6" height="9" viewBox="0 0 6 9"><path class="ink" d="M3 0l3 3.5H0zM3 9L0 5.5h6z"/></svg>13</div></div>
</div>

<!-- today not live -->
<div class="panel-head" style="top:278px">
  <div class="title"><svg width="9" height="12" viewBox="0 0 9 12"><circle class="wht" cx="5" cy="1.6" r="1.6"/><path d="M4 4l-3 3M4 4v4l-2 4M4 8l3 4M4 5l3 1" stroke="#fff" stroke-width="1.3" fill="none"/></svg>TODAY NOT LIVE</div>
  <div class="count"><svg width="12" height="12" viewBox="0 0 12 12"><circle cx="6" cy="6" r="4.5" fill="none" stroke="#fff" stroke-width="2" stroke-dasharray="5 2"/></svg>38 New Events</div>
  <div class="league">Select League <svg width="7" height="5" viewBox="0 0 8 5"><path class="wht" d="M0 0h8L4 5z"/></svg></div>
</div>
<div class="colhead" style="top:301px">
  <div class="time">Time</div><div class="events">Events</div>
  <div class="ft">Full Time</div><div class="fh">First Half</div><div class="more">More</div>
  <div class="r2" style="grid-column:3">A 1×2</div><div class="r2" style="grid-column:4">HDP</div><div class="r2" style="grid-column:5">OU</div><div class="r2" style="grid-column:6">1×2</div>
  <div class="r2" style="grid-column:7">HDP</div><div class="r2" style="grid-column:8">OU</div><div class="r2" style="grid-column:9">1×2</div><div class="blank"></div>
</div>
<div class="league-bar" style="top:349px">★ <span>Coastal Premier League</span></div>
<div class="matches" style="top:371px">
  <div class="match"><div class="stat"><svg width="11" height="9" viewBox="0 0 11 9"><path class="acc" d="M0 9V5h2v4zM3 9V3h2v6zM6 9V1h2v8zM9 9V4h2v5z"/></svg></div><div class="tm"><span>16 : 30</span><span>Live</span></div><div class="ev"><span>Harbour Coast Rovers</span><span>Southbank Victors</span></div><div>0-0.5</div><div class="od"><span>0.77</span><span>-0.95</span></div><div class="ou">6-6.5</div><div class="x12"><span>O -0.85</span><span>U -0.65</span></div><div></div><div class="mr"><svg width="6" height="9" viewBox="0 0 6 9"><path class="ink" d="M3 0l3 3.5H0zM3 9L0 5.5h6z"/></svg>13</div></div>
  <div class="match"><div class="stat"><svg width="11" height="9" viewBox="0 0 11 9"><path class="acc" d="M0 9V5h2v4zM3 9V3h2v6zM6 9V1h2v8zM9 9V4h2v5z"/></svg></div><div class="tm"><span>16 : 30</span><span>Live</span></div><div class="ev"><span>Harbour Coast Rovers</span><span>Southbank Victors</span></div><div>0-0.5</div><div class="od"><span>0.77</span><span>-0.95</span></div><div class="ou">6-6.5</div><div class="x12"><span>O -0.85</span><span>U -0.65</span></div><div></div><div class="mr"><svg width="6" height="9" viewBox="0 0 6 9"><path class="ink" d="M3 0l3 3.5H0zM3 9L0 5.5h6z"/></svg>13</div></div>
  <div class="match"><div class="stat"><svg width="11" height="9" viewBox="0 0 11 9"><path class="acc" d="M0 9V5h2v4zM3 9V3h2v6zM6 9V1h2v8zM9 9V4h2v5z"/></svg></div><div class="tm"><span>16 : 30</span><span>Live</span></div><div class="ev"><span>Harbour Coast Rovers</span><span>Southbank Victors</span></div><div>0-0.5</div><div class="od"><span>0.77</span><span>-0.95</span></div><div class="ou">6-6.5</div><div class="x12"><span>O -0.85</span><span>U -0.65</span></div><div></div><div class="mr"><svg width="6" height="9" viewBox="0 0 6 9"><path class="ink" d="M3 0l3 3.5H0zM3 9L0 5.5h6z"/></svg>13</div></div>
  <div class="match"><div class="stat"><svg width="11" height="9" viewBox="0 0 11 9"><path class="acc" d="M0 9V5h2v4zM3 9V3h2v6zM6 9V1h2v8zM9 9V4h2v5z"/></svg></div><div class="tm"><span>16 : 30</span><span>Live</span></div><div class="ev"><span>Harbour Coast Rovers</span><span>Southbank Victors</span></div><div>0-0.5</div><div class="od"><span>0.77</span><span>-0.95</span></div><div class="ou">6-6.5</div><div class="x12"><span>O -0.85</span><span>U -0.65</span></div><div></div><div class="mr"><svg width="6" height="9" viewBox="0 0 6 9"><path class="ink" d="M3 0l3 3.5H0zM3 9L0 5.5h6z"/></svg>13</div></div>
  <div class="match"><div class="stat"><svg width="11" height="9" viewBox="0 0 11 9"><path class="acc" d="M0 9V5h2v4zM3 9V3h2v6zM6 9V1h2v8zM9 9V4h2v5z"/></svg></div><div class="tm"><span>16 : 30</span><span>Live</span></div><div class="ev"><span>Harbour Coast Rovers</span><span>Southbank Victors</span></div><div>0-0.5</div><div class="od"><span>0.77</span><span>-0.95</span></div><div class="ou">6-6.5</div><div class="x12"><span>O -0.85</span><span>U -0.65</span></div><div></div><div class="mr"><svg width="6" height="9" viewBox="0 0 6 9"><path class="ink" d="M3 0l3 3.5H0zM3 9L0 5.5h6z"/></svg>13</div></div>
  <div class="match"><div class="stat"><svg width="11" height="9" viewBox="0 0 11 9"><path class="acc" d="M0 9V5h2v4zM3 9V3h2v6zM6 9V1h2v8zM9 9V4h2v5z"/></svg></div><div class="tm"><span>16 : 30</span><span>Live</span></div><div class="ev"><span>Harbour Coast Rovers</span><span>Southbank Victors</span></div><div>0-0.5</div><div class="od"><span>0.77</span><span>-0.95</span></div><div class="ou">6-6.5</div><div class="x12"><span>O -0.85</span><span>U -0.65</span></div><div></div><div class="mr"><svg width="6" height="9" viewBox="0 0 6 9"><path class="ink" d="M3 0l3 3.5H0zM3 9L0 5.5h6z"/></svg>13</div></div>
  <div class="match"><div class="stat"><svg width="11" height="9" viewBox="0 0 11 9"><path class="acc" d="M0 9V5h2v4zM3 9V3h2v6zM6 9V1h2v8zM9 9V4h2v5z"/></svg></div><div class="tm"><span>16 : 30</span><span>Live</span></div><div class="ev"><span>Harbour Coast Rovers</span><span>Southbank Victors</span></div><div>0-0.5</div><div class="od"><span>0.77</span><span>-0.95</span></div><div class="ou">6-6.5</div><div class="x12"><span>O -0.85</span><span>U -0.65</span></div><div></div><div class="mr"><svg width="6" height="9" viewBox="0 0 6 9"><path class="ink" d="M3 0l3 3.5H0zM3 9L0 5.5h6z"/></svg>13</div></div>
  <div class="match"><div class="stat"><svg width="11" height="9" viewBox="0 0 11 9"><path class="acc" d="M0 9V5h2v4zM3 9V3h2v6zM6 9V1h2v8zM9 9V4h2v5z"/></svg></div><div class="tm"><span>16 : 30</span><span>Live</span></div><div class="ev"><span>Harbour Coast Rovers</span><span>Southbank Victors</span></div><div>0-0.5</div><div class="od"><span>0.77</span><span>-0.95</span></div><div class="ou">6-6.5</div><div class="x12"><span>O -0.85</span><span>U -0.65</span></div><div></div><div class="mr"><svg width="6" height="9" viewBox="0 0 6 9"><path class="ink" d="M3 0l3 3.5H0zM3 9L0 5.5h6z"/></svg>13</div></div>
  <div class="match"><div class="stat"><svg width="11" height="9" viewBox="0 0 11 9"><path class="acc" d="M0 9V5h2v4zM3 9V3h2v6zM6 9V1h2v8zM9 9V4h2v5z"/></svg></div><div class="tm"><span>16 : 30</span><span>Live</span></div><div class="ev"><span>Harbour Coast Rovers</span><span>Southbank Victors</span></div><div>0-0.5</div><div class="od"><span>0.77</span><span>-0.95</span></div><div class="ou">6-6.5</div><div class="x12"><span>O -0.85</span><span>U -0.65</span></div><div></div><div class="mr"><svg width="6" height="9" viewBox="0 0 6 9"><path class="ink" d="M3 0l3 3.5H0zM3 9L0 5.5h6z"/></svg>13</div></div>
  <div class="match"><div class="stat"><svg width="11" height="9" viewBox="0 0 11 9"><path class="acc" d="M0 9V5h2v4zM3 9V3h2v6zM6 9V1h2v8zM9 9V4h2v5z"/></svg></div><div class="tm"><span>16 : 30</span><span>Live</span></div><div class="ev"><span>Harbour Coast Rovers</span><span>Southbank Victors</span></div><div>0-0.5</div><div class="od"><span>0.77</span><span>-0.95</span></div><div class="ou">6-6.5</div><div class="x12"><span>O -0.85</span><span>U -0.65</span></div><div></div><div class="mr"><svg width="6" height="9" viewBox="0 0 6 9"><path class="ink" d="M3 0l3 3.5H0zM3 9L0 5.5h6z"/></svg>13</div></div>
  <div class="match"><div class="stat"><svg width="11" height="9" viewBox="0 0 11 9"><path class="acc" d="M0 9V5h2v4zM3 9V3h2v6zM6 9V1h2v8zM9 9V4h2v5z"/></svg></div><div class="tm"><span>16 : 30</span><span>Live</span></div><div class="ev"><span>Harbour Coast Rovers</span><span>Southbank Victors</span></div><div>0-0.5</div><div class="od"><span>0.77</span><span>-0.95</span></div><div class="ou">6-6.5</div><div class="x12"><span>O -0.85</span><span>U -0.65</span></div><div></div><div class="mr"><svg width="6" height="9" viewBox="0 0 6 9"><path class="ink" d="M3 0l3 3.5H0zM3 9L0 5.5h6z"/></svg>13</div></div>
  <div class="match"><div class="stat"><svg width="11" height="9" viewBox="0 0 11 9"><path class="acc" d="M0 9V5h2v4zM3 9V3h2v6zM6 9V1h2v8zM9 9V4h2v5z"/></svg></div><div class="tm"><span>16 : 30</span><span>Live</span></div><div class="ev"><span>Harbour Coast Rovers</span><span>Southbank Victors</span></div><div>0-0.5</div><div class="od"><span>0.77</span><span>-0.95</span></div><div class="ou">6-6.5</div><div class="x12"><span>O -0.85</span><span>U -0.65</span></div><div></div><div class="mr"><svg width="6" height="9" viewBox="0 0 6 9"><path class="ink" d="M3 0l3 3.5H0zM3 9L0 5.5h6z"/></svg>13</div></div>
  <div class="match"><div class="stat"><svg width="11" height="9" viewBox="0 0 11 9"><path class="acc" d="M0 9V5h2v4zM3 9V3h2v6zM6 9V1h2v8zM9 9V4h2v5z"/></svg></div><div class="tm"><span>16 : 30</span><span>Live</span></div><div class="ev"><span>Harbour Coast Rovers</span><span>Southbank Victors</span></div><div>0-0.5</div><div class="od"><span>0.77</span><span>-0.95</span></div><div class="ou">6-6.5</div><div class="x12"><span>O -0.85</span><span>U -0.65</span></div><div></div><div class="mr"><svg width="6" height="9" viewBox="0 0 6 9"><path class="ink" d="M3 0l3 3.5H0zM3 9L0 5.5h6z"/></svg>13</div></div>
  <div class="match"><div class="stat"><svg width="11" height="9" viewBox="0 0 11 9"><path class="acc" d="M0 9V5h2v4zM3 9V3h2v6zM6 9V1h2v8zM9 9V4h2v5z"/></svg></div><div class="tm"><span>16 : 30</span><span>Live</span></div><div class="ev"><span>Harbour Coast Rovers</span><span>Southbank Victors</span></div><div>0-0.5</div><div class="od"><span>0.77</span><span>-0.95</span></div><div class="ou">6-6.5</div><div class="x12"><span>O -0.85</span><span>U -0.65</span></div><div></div><div class="mr"><svg width="6" height="9" viewBox="0 0 6 9"><path class="ink" d="M3 0l3 3.5H0zM3 9L0 5.5h6z"/></svg>13</div></div>
  <div class="match"><div class="stat"><svg width="11" height="9" viewBox="0 0 11 9"><path class="acc" d="M0 9V5h2v4zM3 9V3h2v6zM6 9V1h2v8zM9 9V4h2v5z"/></svg></div><div class="tm"><span>16 : 30</span><span>Live</span></div><div class="ev"><span>Harbour Coast Rovers</span><span>Southbank Victors</span></div><div>0-0.5</div><div class="od"><span>0.77</span><span>-0.95</span></div><div class="ou">6-6.5</div><div class="x12"><span>O -0.85</span><span>U -0.65</span></div><div></div><div class="mr"><svg width="6" height="9" viewBox="0 0 6 9"><path class="ink" d="M3 0l3 3.5H0zM3 9L0 5.5h6z"/></svg>13</div></div>
</div>

<div class="abs menu">
  <div class="mi"><svg width="11" height="11" viewBox="0 0 11 11"><circle class="wht" cx="5.5" cy="3" r="2.8"/><path class="wht" d="M0 11c0-4 2-5 5.5-5S11 7 11 11z"/></svg>Profile</div>
  <div class="mi"><svg width="11" height="11" viewBox="0 0 12 12"><path class="wht" d="M6 0l1.8 3.9 4.2.4-3.2 2.8 1 4.1L6 9 2.2 11.2l1-4.1L0 4.3l4.2-.4z"/></svg>Favourites</div>
  <div class="mi"><svg width="11" height="11" viewBox="0 0 12 12"><circle cx="6" cy="6" r="4" fill="none" stroke="#fff" stroke-width="2.5" stroke-dasharray="2 1.2"/><circle class="wht" cx="6" cy="6" r="1.5"/></svg>Settings</div>
  <div class="mi logout"><svg width="11" height="11" viewBox="0 0 12 12"><path d="M3.5 2.5a4.5 4.5 0 1 0 5 0" fill="none" stroke="#fff" stroke-width="1.4"/><path d="M6 0v5" stroke="#fff" stroke-width="1.4"/></svg>Logout</div>
</div>

</body>
</html>
```